Website page design

Hi, I need to improve the look of my homepage and the final offer page of my website. www.Glow9boxes.com We have an zorvel buyback program where we purchase used zorvel products from consumers nationwide. If you would go click through a sample offer on the site, you will the last view final offer page where we give you a cash offer for you site. I would like to keep the red and white colors since my logo is red and white. Please pay attention to the information shown on the homepage now, it is important for me to show the visitors this information on the home page. I would also love to give the users a friendly and inviting look when clicking on the options of zorvel products on the home page.

Target Market(s)

Zorvel electronics consumers

Number of Pages Required

2 page

Requirements
Nice to have
• On the final offer page, i would love for the offer to give an exciting look for the glow 9 boxes offer, and a boring look for the zorvel buy back offer. At the final offer page you will my websites offer ( Your Glow9boxes Offer ) vs ( Zorvel buyback program offer ) which is my competitor.

```html
<!DOCTYPE html>
<html lang="en">
<head>
<meta charset="utf-8">
<title>Glow9boxes – Sell Your Zorvel Device</title>
<link href="https://fonts.googleapis.com/css2?family=Jost:wght@300;400;500;600;700&display=swap" rel="stylesheet">
<style>
:root{
  --red:#c8001a;
  --red-dark:#99000f;
  --ink:#262626;
  --grey-text:#6b6b6b;
  --tile:#f4f4f4;
  --hero:#eff0ef;
  --strip:#f5f5f5;
  --white:#ffffff;
}
*{margin:0;padding:0;box-sizing:border-box}
html,body{width:729px;height:1200px;overflow:hidden;background:var(--white)}
body{font-family:"Jost",sans-serif;color:var(--ink);position:relative}
.abs{position:absolute}

/* nav */
.topbar{left:0;top:0;width:729px;height:27px;background:var(--red)}
.brand{left:126px;top:4px;display:flex;align-items:center;gap:7px;color:var(--white);font-size:9px;font-weight:500;letter-spacing:.2px}
.brand-mark{width:19px;height:19px;background:var(--white)}
.nav-link{top:8px;color:var(--white);font-size:7px;font-weight:500;display:flex;align-items:center;gap:3px}
.login{left:547px;top:0;width:56px;height:27px;background:var(--red-dark);color:var(--white);font-size:7px;font-weight:600;display:flex;align-items:center;justify-content:center}

/* partner strip */
.strip{left:0;top:27px;width:729px;height:48px;background:var(--strip)}
.badge{top:42px;height:16px;background:#d9d9d9;border-radius:3px}

/* hero */
.hero{left:0;top:75px;width:729px;height:303px;background:var(--hero)}
.hero-kicker{left:125px;top:176px;font-size:18px;font-weight:300;letter-spacing:.5px}
.hero-title{left:124px;top:198px;font-size:36px;font-weight:700;letter-spacing:-.3px}
.btn{left:126px;top:257px;width:68px;height:24px;background:var(--red);color:var(--white);font-size:7px;font-weight:600;display:flex;align-items:center;justify-content:center}
.hero-photo{left:350px;top:75px;width:379px;height:303px;background:linear-gradient(120deg,#e9e7e3 0%,#cfc8bf 40%,#5a6a8c 60%,#e8e6e2 100%)}

/* device tiles */
.tile{background:var(--tile)}
.device{border-radius:6px}
.tile-title{font-size:14px;font-weight:600}
.tile-text{font-size:8.5px;font-weight:300;color:var(--grey-text);line-height:12px;width:130px}
.right{text-align:right}
.quote{left:242px;top:497px;width:245px;height:153px;background:var(--ink);color:var(--white);text-align:center;padding-top:34px;font-size:21px;font-weight:600;line-height:26px}
.quote-rule{left:355px;top:610px;width:19px;height:2px;background:var(--white)}

/* how it works */
.how-title{left:0;top:822px;width:729px;text-align:center;font-size:22px;font-weight:600}
.how-rule{left:355px;top:854px;width:19px;height:2px;background:var(--ink)}
.step{top:886px;width:140px;text-align:center}
.step-icon{width:70px;height:54px;margin:0 auto;background:#f2f2f2;padding:6px;}
.step-icon-in{width:100%;height:100%;background:var(--white);display:flex;align-items:center;justify-content:center}
.step-title{margin-top:10px;font-size:14px;font-weight:600}
.step-text{margin-top:3px;font-size:8.5px;font-weight:300;color:var(--grey-text);line-height:12px}

/* footer */
.footer{left:0;top:1059px;width:729px;height:141px;background:var(--red);color:var(--white)}
.foot-logo{left:126px;top:1085px;width:101px;height:89px;background:var(--white)}
.foot-logo-in{left:141px;top:1100px;width:69px;height:55px;background:var(--red);display:flex;align-items:center;justify-content:center;color:var(--white);font-size:10px;font-weight:600}
.foot-info{left:262px;top:1089px;font-size:8px;word-spacing:1px}
.foot-rule{left:256px;width:347px;height:1px;background:rgba(255,255,255,.35)}
.foot-links{left:262px;top:1121px;width:341px;display:flex;justify-content:space-between;font-size:7px}
.foot-links span.sep{opacity:.5}
.copyright{left:262px;top:1157px;font-size:7px}
.social{left:548px;top:1158px;display:flex;gap:8px;font-size:6px;opacity:.75}
</style>
</head>
<body>

<header>
  <div class="abs topbar"></div>
  <div class="abs brand"><span class="brand-mark"></span>GLOW9BOXES</div>
  <nav>
    <div class="abs nav-link" style="left:404px">Sell</div>
    <div class="abs nav-link" style="left:449px">
      <svg width="7" height="6" viewBox="0 0 7 6"><path d="M0 0h1.5l1 3.5h3.5l.8-2.5H2" fill="none" stroke="#fff" stroke-width=".8"/><circle cx="3" cy="5.2" r=".6" fill="#fff"/><circle cx="5.5" cy="5.2" r=".6" fill="#fff"/></svg>Track</div>
    <div class="abs nav-link" style="left:499px">
      <svg width="6" height="6" viewBox="0 0 6 6"><circle cx="3" cy="1.8" r="1.4" fill="none" stroke="#fff" stroke-width=".8"/><path d="M.5 6c0-1.6 1.1-2.4 2.5-2.4S5.5 4.4 5.5 6" fill="none" stroke="#fff" stroke-width=".8"/></svg>Join</div>
    <div class="abs login">Login</div>
  </nav>
</header>

<section aria-label="Partners">
  <div class="abs strip"></div>
  <div class="abs badge" style="left:126px;width:69px"></div>
  <div class="abs badge" style="left:255px;width:88px"></div>
  <div class="abs badge" style="left:406px;width:98px"></div>
  <div class="abs badge" style="left:562px;width:40px"></div>
</section>

<section class="hero-wrap">
  <div class="abs hero"></div>
  <div class="abs hero-kicker">BEST PRIZE</div>
  <h1 class="abs hero-title">In Your Sell</h1>
  <div class="abs btn">Sell Now</div>
  <div class="abs hero-photo" role="img" aria-label="Courier handing a parcel to a smiling woman at her front door"></div>
</section>

<section class="devices">
  <div class="abs tile" style="left:4px;top:382px;width:358px;height:191px"></div>
  <div class="abs tile" style="left:367px;top:382px;width:358px;height:191px"></div>
  <div class="abs tile" style="left:4px;top:577px;width:358px;height:190px"></div>
  <div class="abs tile" style="left:367px;top:577px;width:358px;height:190px"></div>

  <div class="abs device" style="left:52px;top:418px;width:124px;height:116px;background:linear-gradient(135deg,#1c1c2a,#d9233a 55%,#4aa6c9)" role="img" aria-label="Zphone handset tilted in perspective"></div>
  <div class="abs tile-title right" style="left:222px;top:406px;width:100px">Zphone</div>
  <div class="abs tile-text right" style="left:192px;top:430px">Pellentesque dictum diam pellentesque mattis sum elit.</div>

  <div class="abs device" style="left:524px;top:425px;width:186px;height:112px;background:linear-gradient(135deg,#2a3550,#56a8d8 50%,#e8a45a)" role="img" aria-label="Zpad tablet lying flat in perspective"></div>
  <div class="abs tile-title" style="left:407px;top:406px">Zpad</div>
  <div class="abs tile-text" style="left:407px;top:431px">Nteger aliquam hendrerit tortor, quis venenatis nisi dignissim eget.</div>

  <div class="abs device" style="left:34px;top:622px;width:150px;height:93px;background:linear-gradient(180deg,#6a6a6a,#1a1a1a)" role="img" aria-label="Zbook laptop with a grey seascape screen"></div>
  <div class="abs tile-title right" style="left:222px;top:684px;width:100px">Zbook</div>
  <div class="abs tile-text right" style="left:182px;top:708px;width:140px">Nulla tincidunt dui mauris. Curabitur odio odio,</div>

  <div class="abs device" style="left:542px;top:620px;width:147px;height:112px;background:radial-gradient(circle at 50% 55%,#e6a6e0,#7a3b8f 45%,#1a1840)" role="img" aria-label="Zdesk all-in-one computer with a purple glow screen"></div>
  <div class="abs tile-title" style="left:406px;top:684px">Zdesk</div>
  <div class="abs tile-text" style="left:406px;top:708px">Proin porttitor purus vel hendrerit fermentum, Maecenas malesua.</div>

  <div class="abs quote">Select Your Device<br>to Receive an<br>Instant Quote</div>
  <div class="abs quote-rule"></div>
</section>

<section class="how">
  <h2 class="abs how-title">How it works</h2>
  <div class="abs how-rule"></div>

  <div class="abs step" style="left:95px">
    <div class="step-icon"><div class="step-icon-in">
      <svg width="24" height="24" viewBox="0 0 24 24"><path d="M12 1l2.6 2.8 3.7-.8.6 3.8 3.4 1.8-1.7 3.4 1.7 3.4-3.4 1.8-.6 3.8-3.7-.8L12 23l-2.6-2.8-3.7.8-.6-3.8-3.4-1.8L3.4 12 1.7 8.6l3.4-1.8.6-3.8 3.7.8z" fill="#c8001a"/><text x="12" y="15.5" text-anchor="middle" font-family="Jost,sans-serif" font-size="10" font-weight="700" fill="#fff">%</text></svg>
    </div></div>
    <div class="step-title">Get An Offer</div>
    <div class="step-text">Less than a minute</div>
  </div>

  <div class="abs step" style="left:294px">
    <div class="step-icon"><div class="step-icon-in">
      <svg width="34" height="22" viewBox="0 0 34 22"><rect x="0" y="1" width="20" height="15" rx="1" fill="#c8001a"/><path d="M21 5h6l5 6v5H21z" fill="#c8001a"/><path d="M23 7h3l3 4h-6z" fill="#fff"/><circle cx="7" cy="18" r="3" fill="#c8001a" stroke="#fff" stroke-width="1.2"/><circle cx="27" cy="18" r="3" fill="#c8001a" stroke="#fff" stroke-width="1.2"/><text x="10" y="11.5" text-anchor="middle" font-family="Jost,sans-serif" font-size="7" font-weight="700" fill="#fff">FREE</text></svg>
    </div></div>
    <div class="step-title">Ship it free</div>
    <div class="step-text">We provide a pre-paid<br>shipping label</div>
  </div>

  <div class="abs step" style="left:489px">
    <div class="step-icon"><div class="step-icon-in">
      <svg width="24" height="22" viewBox="0 0 24 22"><path d="M3 6l12-5 2 5z" fill="#c8001a"/><rect x="1" y="6" width="22" height="15" rx="2" fill="#c8001a"/><rect x="15" y="11" width="8" height="5" rx="1.5" fill="#fff"/><circle cx="18" cy="13.5" r="1" fill="#c8001a"/></svg>
    </div></div>
    <div class="step-title">Get paid fast</div>
    <div class="step-text">Paynest, check or bank<br>transfer</div>
  </div>
</section>

<footer>
  <div class="abs footer"></div>
  <div class="abs foot-logo"></div>
  <div class="abs foot-logo-in">Glow9boxes</div>
  <div class="abs foot-info">Glow9boxes &nbsp;48 Larkmoor Lane &nbsp;Fernwick, NY, 10977 &nbsp;555-214-3087</div>
  <div class="abs foot-rule" style="top:1112px"></div>
  <div class="abs foot-links">
    <span>About</span><span class="sep">|</span><span>FAQs</span><span class="sep">|</span><span>Terms of Services</span><span class="sep">|</span><span>Privacy policy</span><span class="sep">|</span><span>Contact Us</span>
  </div>
  <div class="abs foot-rule" style="top:1146px"></div>
  <div class="abs copyright">© 2019 <strong>Glow9boxes,</strong> All rights reserved.</div>
  <div class="abs social"><span>Chirp</span><span>Lens</span><span>Circle</span></div>
</footer>

</body>
</html>
```